New website

We ned to create a new website that reflects more who we are. We are delivering exclusive premium products to our customers and the current website does not reflect our products at all.
We believe in less is more and need a webpage that is clean yet professional and exclusive.

Target Market(s)

Dentistry

Industry/Entity Type

Dental

Number of Pages Required

5+ page

Font styles to use
Sans Serif

Colors

Designer to choose colors to be used in the design.

Requirements
Must have
• Picture gallery
• Nice structure
• Clean layout
Nice to have
• Light fonts
Should not have
• Any italic font styles

```html
<!DOCTYPE html>
<html lang="en">
<head>
<meta charset="utf-8">
<title>Lumadent — Welcome</title>
<link rel="stylesheet" href="https://fonts.googleapis.com/css2?family=Montserrat:wght@300;400;500;700&family=Open+Sans:wght@300;400;600&display=swap">
<style>
  :root {
    --teal: #24c6d4;
    --teal-bright: #2ee6dc;
    --navy: #293346;
    --coral: #ee5b56;
    --ink: #4a4f57;
    --white: #ffffff;
    --slate: #6f7a8a;
  }
  * { margin: 0; padding: 0; box-sizing: border-box; }
  html, body { width: 1000px; height: 1200px; overflow: hidden; background: var(--white); }
  body { position: relative; font-family: "Open Sans", sans-serif; color: var(--ink); }

  .hero { position: absolute; left: 0; top: 0; width: 1000px; height: 562px; overflow: hidden; }
  .hero-photo {
    position: absolute; inset: 0;
    background:
      radial-gradient(ellipse at 70% 40%, rgba(120,240,230,0.55), transparent 60%),
      linear-gradient(90deg, var(--teal-bright) 0%, #1fcfc6 45%, #17a9a6 100%);
  }
  .brand {
    position: absolute; left: 36px; top: 58px;
    font-family: "Montserrat", sans-serif; font-weight: 300; font-size: 15px;
    letter-spacing: 9px; color: var(--white);
  }
  .brand-mark { position: absolute; left: 84px; top: 35px; width: 16px; height: 16px; background: var(--white); }
  .nav { position: absolute; left: 240px; top: 63px; display: flex; gap: 19px; list-style: none; }
  .nav li { font-family: "Montserrat", sans-serif; font-size: 10px; font-weight: 500; letter-spacing: 0.8px; color: var(--white); }
  .nav li.active { color: var(--navy); }
  .lang { position: absolute; right: 38px; top: 33px; font-family: "Montserrat", sans-serif; font-size: 8px; font-weight: 600; color: var(--white); }
  .lang .current { color: var(--coral); }

  .hero-title { position: absolute; left: 85px; top: 283px; }
  .hero-title .light { display: block; font-family: "Montserrat", sans-serif; font-weight: 300; font-size: 34px; color: var(--white); line-height: 1; letter-spacing: -0.5px; }
  .hero-title .bold { display: block; font-family: "Montserrat", sans-serif; font-weight: 700; font-size: 41px; color: var(--navy); letter-spacing: 4px; line-height: 1.1; }
  .slider-dots { position: absolute; left: 85px; top: 383px; display: flex; gap: 5px; }
  .slider-dots span { width: 7px; height: 7px; border-radius: 50%; border: 1px solid var(--white); }
  .slider-dots span.on { background: var(--white); }
  .scroll-cue { position: absolute; left: 481px; top: 467px; }

  .welcome { position: absolute; left: 85px; top: 600px; width: 420px; }
  .section-title { font-family: "Montserrat", sans-serif; font-weight: 300; font-size: 22px; color: var(--ink); letter-spacing: -0.3px; }
  .section-title strong { font-weight: 700; color: var(--coral); letter-spacing: 2px; }
  .welcome p { font-size: 10.5px; font-weight: 300; line-height: 16px; margin-top: 16px; }
  .welcome p.lead { margin-top: 14px; }

  .gallery-card { position: absolute; left: 585px; top: 604px; width: 330px; height: 237px; }
  .gallery-photo { height: 182px; background: linear-gradient(90deg, #6d7787 0%, #7d8797 55%, #a8aebb 100%); }
  .gallery-caption { height: 55px; background: var(--navy); color: var(--white); font-size: 10.5px; text-align: center; padding-top: 14px; line-height: 14px; }
  .gallery-caption a { color: var(--teal); }

  .smiles { position: absolute; left: 85px; top: 866px; }
  .smiles p { font-size: 10.5px; font-weight: 300; margin-top: 14px; }

  .tiles { position: absolute; left: 0; top: 959px; width: 1000px; height: 165px; display: flex; }
  .tile { flex: 1; display: flex; flex-direction: column; align-items: center; padding-top: 60px; color: var(--white);
    font-family: "Montserrat", sans-serif; font-size: 15px; letter-spacing: 1.5px; }
  .tile i { display: block; width: 14px; height: 14px; background: var(--white); margin-bottom: 12px; }
  .tile.teal { background: var(--teal); }
  .tile.navy { background: var(--navy); }

  .footer { position: absolute; left: 0; top: 1124px; width: 1000px; height: 76px; background: var(--coral);
    color: var(--white); font-size: 8px; text-align: center; padding-top: 28px; }
</style>
</head>
<body>
  <header class="hero">
    <div class="hero-photo" role="img" aria-label="Photo of a smiling young woman and an older woman cheek to cheek, tinted turquoise"></div>
    <span class="brand-mark"></span>
    <div class="brand">LUMADENT</div>
    <ul class="nav">
      <li class="active">WELCOME</li><li>PRODUCTS</li><li>SPECIAL SERVICES</li><li>SMILE GALLERY</li><li>THE COMPANY</li><li>SHADE ANALYSIS</li><li>CONTACT</li>
    </ul>
    <div class="lang"><span class="current">ENG</span> | SWE</div>
    <h1 class="hero-title"><span class="light">LUMADENT &amp;</span><span class="bold">CONFIDENCE</span></h1>
    <div class="slider-dots"><span></span><span></span><span></span><span class="on"></span></div>
    <svg class="scroll-cue" width="38" height="70" viewBox="0 0 38 70" aria-hidden="true">
      <circle cx="19" cy="6" r="3" fill="#fff" opacity="0.6"/>
      <circle cx="19" cy="18" r="4" fill="#fff" opacity="0.85"/>
      <circle cx="19" cy="51" r="17" fill="none" stroke="#fff" stroke-width="2"/>
      <path d="M12 50 Q19 56 26 50" fill="none" stroke="#fff" stroke-width="2"/>
    </svg>
  </header>

  <section class="welcome">
    <h2 class="section-title">WELCOME TO <strong>LUMADENT</strong></h2>
    <p class="lead">Who designed this Smile?</p>
    <p>Lumadent smiles has a very distinctive appearance and character.<br>Both these Lumadent features owe as much to their owners as to our dental artisans, because in the final analysis, people who buy a new smile also designs them.</p>
    <p>Inevitably, the greater the demands a smile has to meet, the lower the lowest denominator.</p>
    <p>That's why standard production line smiles have such little character. With our high strength ceramics our aim has never been to create less expensive smiles for the majority, but the perfect smile for few.<br>Isn't it time you joined the few?</p>
  </section>

  <aside class="gallery-card">
    <div class="gallery-photo" role="img" aria-label="Photo of a smiling young couple"></div>
    <div class="gallery-caption">You can see some Lumadent smiles by<br>clicking on <a href="#">Smile Gallery</a>.</div>
  </aside>

  <section class="smiles">
    <h2 class="section-title"><strong>LUMADENT</strong> SMILES</h2>
    <p>The Lumadent range of fine smiles: ultimate in function, comfort and aesthetics.</p>
  </section>

  <nav class="tiles">
    <div class="tile teal"><i></i>PRODUCTS</div>
    <div class="tile navy"><i></i>SPECIAL SERVICES</div>
    <div class="tile teal"><i></i>SMILE GALLERY</div>
    <div class="tile navy"><i></i>CONTACT</div>
  </nav>

  <footer class="footer">Lumadent AB &nbsp;·&nbsp; Box 51870 &nbsp;·&nbsp; 21530 Norrvik, Sverige &nbsp;·&nbsp; Tel: +46-40-12 34 56</footer>
</body>
</html>
```